glow 482 is renewing its image

more dynamic website, make it look more attractive for the services we offer, at the same time more accurate on the services description. We want people to know we offer treatments that big corporations offer but not as expensive as they offer it. prices will be add by me once the website is approve

already have a website with wix.com www.glow482skin.com

Target Market(s)

women between 21 to 75

Industry/Entity Type

beauty services, body contouring

Colors

Designer to choose colors to be used in the design.

Requirements
Must have
• pictures of treatments
Nice to have
• accurate information about treatmnets, treatments menu
Should not have
• no online shopping

```html
<!DOCTYPE html>
<html lang="en">
<head>
<meta charset="utf-8">
<title>glow 482 Skin Lounge</title>
<link href="https://fonts.googleapis.com/css2?family=Satisfy&family=Questrial&family=Montserrat:wght@400;600;700&display=swap" rel="stylesheet">
<style>
:root{
  --backdrop-top:#c3a3ab;
  --backdrop-bottom:#a095a3;
  --ink-dark:#2c3239;
  --gold:#b98a5f;
  --gold-deep:#8a5a33;
  --cream:#f8f4f1;
  --white:#ffffff;
  --plum:#7b5668;
  --footer:#23231f;
  --text:#4a4a4a;
  --muted:#c9a98c;
}
*{box-sizing:border-box;margin:0;padding:0}
html,body{width:1200px;height:3599px;overflow:hidden}
body{background:linear-gradient(180deg,var(--backdrop-top),#c9a9b0 50%,var(--backdrop-bottom));font-family:"Questrial",sans-serif;color:var(--text)}
.page{position:absolute;left:198px;top:46px;width:804px;height:3509px;background:var(--white);box-shadow:0 10px 40px rgba(60,30,45,.35);overflow:hidden}
.abs{position:absolute}
.script{font-family:"Satisfy",cursive;color:var(--gold);font-weight:400}
.photo{position:absolute}
.btn{position:absolute;display:flex;align-items:center;justify-content:center;font-family:"Montserrat",sans-serif;font-weight:600;font-size:7px;letter-spacing:.2px}
.btn-gold{background:var(--gold);color:var(--white)}
.btn-white{background:var(--white);color:var(--gold);box-shadow:0 2px 6px rgba(0,0,0,.12)}
.body-copy{font-size:8.5px;line-height:14.5px;color:var(--text)}

/* header */
.header-panel{left:0;top:0;width:410px;height:298px;background:var(--ink-dark)}
.brand{position:absolute;text-align:center;color:var(--gold)}
.brand-name{font-family:"Questrial",sans-serif;font-size:30px;letter-spacing:1px;line-height:1}
.brand-sub{font-size:9px;letter-spacing:1px;margin-top:4px;color:var(--gold)}
.brand-dot{display:inline-block;width:10px;height:10px;border-radius:50%;background:var(--gold);margin-right:8px;vertical-align:middle}
.welcome{left:90px;top:202px;width:230px;text-align:center;font-family:"Satisfy",cursive;color:var(--white);font-size:15px;line-height:24px}
.nav{position:absolute;left:360px;top:104px;display:flex;font-size:8.5px;color:var(--ink-dark)}
.nav span{padding:0 13px;border-left:1px solid #ddd}
.nav span:first-child{border-left:none}
.hero-photo{left:330px;top:127px;width:414px;height:277px;background:linear-gradient(120deg,#6b4a36,#c48f6a 45%,#e9d8c8 80%,#f3eee7);box-shadow:0 10px 22px rgba(0,0,0,.25)}
.intro{left:108px;top:314px;width:175px;font-size:7.5px;line-height:12.5px}
.read-more{left:239px;top:385px;font-size:8px;color:var(--gold);text-decoration:underline}

/* about */
.about{left:0;top:450px;width:804px;height:454px;background:var(--cream)}
.about-frame{left:57px;top:70px;width:354px;height:339px;border:1px solid var(--muted);border-radius:130px 0 0 0;border-right:none;border-top:none}
.about-photo{left:81px;top:43px;width:330px;height:334px;border-radius:110px 0 0 0;background:linear-gradient(135deg,#3c2a24,#8b4f38 40%,#d8d2cb 70%,#5b3a2c)}
.eyebrow{font-size:10px;color:var(--gold)}

/* advantages */
.adv-item{position:absolute;width:220px;text-align:center}
.adv-icon{width:70px;height:66px;margin:0 auto;display:block}
.adv-title{font-size:11px;color:var(--gold-deep);margin-top:12px;letter-spacing:.3px}
.adv-text{font-size:8.5px;line-height:14.5px;color:var(--muted);margin-top:10px}

/* treatments */
.treatments{left:0;top:1217px;width:804px;height:679px;background:var(--cream)}
.card{position:absolute;width:197px;text-align:center}
.card .photo{position:relative;width:197px;height:228px}
.card-title{font-family:"Montserrat",sans-serif;font-weight:600;font-size:10px;color:var(--gold-deep);margin-top:18px;letter-spacing:.4px}
.card-price{font-size:10px;color:var(--gold-deep);margin-top:8px}

/* featured */
.feature-frame{left:57px;top:84px;width:354px;height:341px;border:1px solid var(--muted);border-right:none;border-bottom-left-radius:0}
.feature-photo{left:81px;top:59px;width:330px;height:333px;border-radius:0 0 70px 0;background:linear-gradient(150deg,#e9e3dd,#c98b60 45%,#8e4e2e 65%,#f1ece6)}

/* reviews */
.reviews{left:0;top:2347px;width:804px;height:211px;background:var(--plum);text-align:center}
.stat{position:absolute;width:150px;text-align:center;color:var(--muted)}
.stat-num{font-size:29px;line-height:1}
.stat-label{font-size:7.5px;margin-top:4px}

/* testimonial */
.testimonial-bg{left:279px;top:2558px;width:525px;height:344px;background:var(--cream)}
.quote{left:389px;top:2655px;width:370px;font-size:17px;line-height:21px;color:var(--gold-deep)}
.arrow-btn{position:absolute;width:20px;height:20px}

/* footer */
.footer{left:0;top:3160px;width:804px;height:324px;background:var(--footer);text-align:center}
.footer-nav{position:absolute;left:0;top:168px;width:804px;display:flex;justify-content:center;font-size:9px;color:#e7e2dc}
.footer-nav span{padding:0 11px;border-left:1px solid #555}
.footer-nav span:first-child{border-left:none}
.footer-contact{position:absolute;left:0;top:202px;width:804px;font-size:7.5px;line-height:17px;color:var(--gold)}
.copyright{left:0;top:3484px;width:804px;height:25px;background:var(--cream);text-align:center;font-size:7px;line-height:25px;color:var(--muted)}
</style>
</head>
<body>
<div class="page">

  <!-- Header -->
  <div class="abs header-panel"></div>
  <div class="brand" style="left:105px;top:120px;width:200px">
    <div class="brand-name"><span class="brand-dot"></span>glow 482</div>
    <div class="brand-sub">Skin lounge</div>
  </div>
  <div class="abs welcome">Welcome to Glow 482 Skin Lounge and Post Liposuction Care</div>

  <nav class="nav"><span>About Us</span><span>Home</span><span>Treatments</span><span>Post Surgery Treatment</span><span>Contact</span><span>More</span></nav>

  <div class="photo hero-photo" role="img" aria-label="Hot stone massage on a client's back with white orchids"></div>
  <svg class="abs" style="left:519px;top:246px" width="38" height="38" viewBox="0 0 38 38">
    <circle cx="19" cy="19" r="18" fill="#222" stroke="#fff" stroke-width="1.5"/>
    <path d="M15 12 L27 19 L15 26 Z" fill="none" stroke="#fff" stroke-width="1.5"/>
  </svg>

  <p class="abs intro">Located in Brookfield, CT, Glow 482 Skin Lounge makes the most of what you've got with services designed to complement your looks and needs.</p>
  <div class="btn btn-white" style="left:108px;top:377px;width:116px;height:25px;color:var(--ink-dark)">Make an Appointment</div>
  <div class="abs read-more">Read More</div>

  <!-- About -->
  <section class="abs about">
    <div class="abs about-frame"></div>
    <div class="photo about-photo" role="img" aria-label="Lounge interior with sign, potted stone fountain plant and reception desk"></div>
    <div class="abs eyebrow" style="left:450px;top:58px">Glow 482 skin lounge</div>
    <h2 class="abs script" style="left:444px;top:78px;font-size:27px;line-height:34px">Beauty Anywhere,<br>Anytime</h2>
    <div class="abs body-copy" style="left:444px;top:146px;width:305px">
      <p>You deserve more, whether it's a suite of services that treats every bodily need, a top-notch professional staff or a relaxing venue to enjoy them in. This is where We shine.</p>
      <p style="margin-top:14px">Here, you can take your pick of from a variety of beauty-boosting services.<br>We use Peruvian natural products. For instance, the Skin Care Body Wraps, which are tailored to relax the body, detoxify, exfoliate and hydrate the skin, all while helping you to lose inches.</p>
      <p style="margin-top:14px">This treatments enhances both your psychological and physical wellness.</p>
    </div>
    <div class="btn btn-white" style="left:444px;top:342px;width:81px;height:25px">Our Services</div>
    <div class="btn btn-gold" style="left:545px;top:342px;width:115px;height:25px">Make an Appointment</div>
  </section>

  <!-- Advantages -->
  <h2 class="abs script" style="left:0;top:944px;width:804px;text-align:center;font-size:28px">Our Advantages</h2>
  <div class="adv-item" style="left:55px;top:1032px">
    <svg class="adv-icon" viewBox="0 0 70 66"><path d="M12 18C20 2 52 0 62 16S64 58 44 62 4 50 8 34 10 22 12 18Z" fill="#f6ede6"/><rect x="24" y="18" width="14" height="28" rx="3" fill="none" stroke="#d4a98a" stroke-width="1.3"/><rect x="27" y="13" width="8" height="5" fill="none" stroke="#d4a98a" stroke-width="1.3"/><circle cx="44" cy="40" r="7" fill="none" stroke="#d4a98a" stroke-width="1.3"/></svg>
    <div class="adv-title">Natural Cosmetic</div>
    <div class="adv-text">We use only natural cosmetics from trusted brands. We always pay attention to the composition of cosmetics.</div>
  </div>
  <div class="adv-item" style="left:294px;top:1032px">
    <svg class="adv-icon" viewBox="0 0 70 66"><path d="M10 20C18 2 54 2 62 18S62 58 42 62 4 52 8 36Z" fill="#f6ede6"/><rect x="24" y="14" width="22" height="32" rx="2" fill="none" stroke="#d4a98a" stroke-width="1.3"/><path d="M35 22v10M30 27h10M28 38h14M28 42h14" stroke="#d4a98a" stroke-width="1.3"/></svg>
    <div class="adv-title">Medical Education</div>
    <div class="adv-text">It is important for us that our clients can trust us and not worry about anything. All our specialists have medical education.</div>
  </div>
  <div class="adv-item" style="left:533px;top:1032px">
    <svg class="adv-icon" viewBox="0 0 70 66"><path d="M14 16C24 0 56 4 62 22S58 60 38 62 6 48 10 32Z" fill="#f6ede6"/><rect x="28" y="12" width="18" height="30" rx="3" fill="none" stroke="#d4a98a" stroke-width="1.3"/><path d="M24 32c0-4 6-4 6 0v8c0 6 10 6 10 0" fill="none" stroke="#d4a98a" stroke-width="1.3"/></svg>
    <div class="adv-title">Cleanness</div>
    <div class="adv-text">We provide our clients with free towels and bathrobes. The accessories undergo a special treatment after each customer.</div>
  </div>

  <!-- Treatments -->
  <section class="abs treatments">
    <div class="card" style="left:59px;top:54px">
      <div class="photo" role="img" aria-label="Client with clay face mask applied by brush" style="background:linear-gradient(150deg,#e6e0da,#b7774e 50%,#efe9e3)"></div>
      <div class="card-title">NATURAL PEEL</div><div class="card-price">$ 79.00</div>
    </div>
    <div class="card" style="left:303px;top:54px">
      <div class="photo" role="img" aria-label="Hands massaging a client's abdomen after surgery" style="background:linear-gradient(160deg,#f2ede8,#c58e69 45%,#b27854 70%,#f4efea)"></div>
      <div class="card-title">POST-SURGERY TREATMENT</div><div class="card-price">$ 79.00</div>
    </div>
    <div class="card" style="left:548px;top:54px">
      <div class="photo" role="img" aria-label="Ultrasound cavitation device on a client's leg" style="background:linear-gradient(160deg,#f1eeec,#d9c0ad 50%,#b99278 70%,#f0ece8)"></div>
      <div class="card-title">ULTRASOUND CAVITATION</div><div class="card-price">$ 79.00</div>
    </div>
    <div class="card" style="left:59px;top:357px">
      <div class="photo" role="img" aria-label="Client lying with lipo-laser pads and device" style="background:linear-gradient(160deg,#eef0f1,#d6d6d7 50%,#cdb19c 70%,#eceded)"></div>
      <div class="card-title">LIPO-LASER</div><div class="card-price">$ 79.00</div>
    </div>
    <div class="card" style="left:303px;top:357px">
      <div class="photo" role="img" aria-label="Esthetician performing diamond microdermabrasion on a client" style="background:linear-gradient(150deg,#3a2a22,#8a6550 40%,#d9d3cd 70%,#6b4c3a)"></div>
      <div class="card-title">DIAMOND MICRODERMOABRASION</div><div class="card-price">$ 79.00</div>
    </div>
    <div class="abs script" style="left:522px;top:415px;width:250px;text-align:center;font-size:16px;line-height:25px;color:var(--ink-dark)">Affordable, Gorgeous and Beauty Which You Deserves of Our Services</div>
    <div class="btn btn-gold" style="left:588px;top:508px;width:114px;height:25px">See More</div>
  </section>

  <!-- Featured service -->
  <div class="abs feature-frame" style="top:1980px;left:57px;width:354px;height:341px;border-right:none"></div>
  <div class="photo feature-photo" style="top:1955px" role="img" aria-label="Client receiving a natural clay peel applied with a brush"></div>
  <div class="abs eyebrow" style="left:447px;top:1953px">Service</div>
  <h2 class="abs script" style="left:444px;top:1970px;font-size:27px;line-height:34px">Maximum<br>Glow 482<br>Natural Peel</h2>
  <div class="photo" style="left:648px;top:1955px;width:97px;height:97px;background:linear-gradient(150deg,#e6e0da,#b7774e 50%,#efe9e3)" role="img" aria-label="Next treatment preview: clay face mask"></div>
  <div class="abs" style="left:648px;top:2062px;font-size:7px;color:var(--ink-dark)">Next Page &#8594;</div>
  <div class="abs" style="left:411px;top:2078px;width:393px;height:1px;background:#e3d5c8"></div>
  <div class="abs" style="left:444px;top:2104px;font-size:21px;color:var(--gold)">$ 49.00</div>
  <p class="abs body-copy" style="left:444px;top:2158px;width:310px;font-size:8px;line-height:14px">NON-ACID, herbal formula that is more effective than traditional acids and that is equivalent to 15 microdermoabrasions without the use of acids or harmful crystals.</p>
  <div class="btn btn-gold" style="left:444px;top:2224px;width:115px;height:25px">Book Now</div>

  <!-- Reviews -->
  <section class="abs reviews">
    <div class="abs" style="left:0;top:46px;width:804px;font-size:10px;color:var(--muted)">Glowing Reviews</div>
    <h2 class="abs script" style="left:0;top:62px;width:804px;font-size:26px">Review for our Services</h2>
    <div class="stat" style="left:105px;top:126px"><div class="stat-num">00</div><div class="stat-label">Years of experiences</div></div>
    <div class="stat" style="left:266px;top:126px"><div class="stat-num">0,000</div><div class="stat-label">Satisfied Customers</div></div>
    <div class="stat" style="left:424px;top:126px"><div class="stat-num">0,000</div><div class="stat-label">Project Completed</div></div>
    <div class="stat" style="left:566px;top:126px"><div class="stat-num">00</div><div class="stat-label">Got Awards</div></div>
  </section>

  <!-- Testimonial -->
  <div class="abs testimonial-bg"></div>
  <svg class="abs" style="left:95px;top:2790px" width="36" height="72" viewBox="0 0 36 72">
    <g fill="#c7b8c9">
      <circle cx="3" cy="3" r="1.3"/><circle cx="13" cy="3" r="1.3"/><circle cx="23" cy="3" r="1.3"/><circle cx="33" cy="3" r="1.3"/>
      <circle cx="3" cy="13" r="1.3"/><circle cx="13" cy="13" r="1.3"/><circle cx="23" cy="13" r="1.3"/><circle cx="33" cy="13" r="1.3"/>
      <circle cx="3" cy="23" r="1.3"/><circle cx="13" cy="23" r="1.3"/><circle cx="23" cy="23" r="1.3"/><circle cx="33" cy="23" r="1.3"/>
      <circle cx="3" cy="33" r="1.3"/><circle cx="13" cy="33" r="1.3"/><circle cx="23" cy="33" r="1.3"/><circle cx="33" cy="33" r="1.3"/>
      <circle cx="3" cy="43" r="1.3"/><circle cx="13" cy="43" r="1.3"/><circle cx="23" cy="43" r="1.3"/><circle cx="33" cy="43" r="1.3"/>
      <circle cx="3" cy="53" r="1.3"/><circle cx="13" cy="53" r="1.3"/><circle cx="23" cy="53" r="1.3"/><circle cx="33" cy="53" r="1.3"/>
      <circle cx="3" cy="63" r="1.3"/><circle cx="13" cy="63" r="1.3"/><circle cx="23" cy="63" r="1.3"/><circle cx="33" cy="63" r="1.3"/>
    </g>
  </svg>
  <div class="photo" style="left:110px;top:2608px;width:225px;height:234px;background:linear-gradient(160deg,#3d4a2a,#7d7d4c 45%,#b8ad7a 75%,#4a4f30)" role="img" aria-label="Featured client sitting in a field of tall grass"></div>
  <div class="abs eyebrow" style="left:389px;top:2626px">Featured client</div>
  <p class="abs quote">"We have been using Lumen Care for some time. We got results via phone, email, everyone is always very courteous. The driver Dale is performing his job with pride and promptness. We have had only few claims and they have always been handled to our satisfaction."</p>
  <div class="abs" style="left:389px;top:2822px;font-size:7px;line-height:9px;color:var(--ink-dark)"><b>Lorem Ipsum</b><br>Founder of Lorem Ipsum</div>
  <svg class="arrow-btn" style="left:690px;top:2822px" viewBox="0 0 20 20"><circle cx="10" cy="10" r="9" fill="none" stroke="#c9a98c"/><path d="M11.5 6.5 8 10l3.5 3.5" fill="none" stroke="#c9a98c" stroke-width="1.2"/></svg>
  <svg class="arrow-btn" style="left:724px;top:2822px" viewBox="0 0 20 20"><circle cx="10" cy="10" r="9" fill="none" stroke="#c9a98c"/><path d="M8.5 6.5 12 10l-3.5 3.5" fill="none" stroke="#c9a98c" stroke-width="1.2"/></svg>

  <!-- Newsletter -->
  <h2 class="abs script" style="left:0;top:2944px;width:804px;text-align:center;font-size:28px">Discover the best Glow482</h2>
  <p class="abs body-copy" style="left:200px;top:2996px;width:404px;text-align:center;font-size:8px;line-height:14.5px">At Glow 482 Skin Lounge we provide high quality skin and body treatments that will make you look great and feel great! With more than 10 years of experience our Esthetician Mara will provide you with the information and the treatment that is right for you and your budget. We are like your personal assistants but for your beauty. You can always call us if you have any questions.</p>
  <div class="abs" style="left:200px;top:3075px;width:401px;height:45px;border:1px solid #e6d8cc;border-radius:6px;background:var(--white);box-shadow:0 3px 8px rgba(0,0,0,.06)"></div>
  <div class="abs" style="left:217px;top:3091px;font-size:10px;color:#d9c6b6">Email address here</div>
  <div class="btn btn-gold" style="left:488px;top:3075px;width:113px;height:45px;border-radius:0 6px 6px 0">Subscribe Now</div>

  <!-- Footer -->
  <footer class="abs footer">
    <div class="brand" style="left:302px;top:80px;width:200px">
      <div class="brand-name" style="font-size:26px"><span class="brand-dot"></span>glow 482</div>
      <div class="brand-sub" style="font-size:8px">Skin lounge</div>
    </div>
    <nav class="footer-nav"><span>About Us</span><span>Home</span><span>Treatments</span><span>Post Surgery Treatment</span><span>Contact</span><span>More</span></nav>
    <div class="footer-contact">18 Alder Lane Brookfield CT 06804<br>Tel: (860) 555-0142 or (860) 555-0187<br>glow482spa@mailbox.com</div>
    <svg class="abs" style="left:363px;top:267px" width="78" height="14" viewBox="0 0 78 14">
      <g fill="var(--gold)"><circle cx="7" cy="7" r="6"/><circle cx="28" cy="7" r="6"/><circle cx="49" cy="7" r="6"/><circle cx="70" cy="7" r="6"/></g>
    </svg>
  </footer>
  <div class="abs copyright">&#169; 2021 Glow482 Skin Lounge. All rights reserved.</div>

</div>
</body>
</html>
```